KVM Contracting services . Building and maintenance services, optic fibre installation

Business cards and logo design.I need a logo that I can use on business cards ,workwear and on my vehicles. I would like the KVM to be the main or larger text and contracting services to be the smaller or less important text.I like monograms, modern designs and repeating patterns symbols. I am also a Gemini and my favourite number is 22 so if this can be any inspiration to help with the design. Am thinking of the using German flag colours as a his is my family’s heritage. And the other 2 main colours I wear is black and white.But any ideas are appreciated.I do not need a design that is trade specific but a design that could be used for any business.

Target Market(s)

General public

Contact Information for Business Card

KVM Contracting Services ( front of business card)

(Back of business card)
Marcus Dellwood
0419274530
Maintenance services
Optic fibre and data installation

Logo Text

Logo can just be pattern or monogram or incorporate KVM . I like the gemini star sign and the number 22

Colors
ec1f27
000000
fbee3e
ffffff

Requirements
Must have
• Logo and KVM Contracting Services on the front of business card
Nice to have
• Possible use of German flag colours.
• Modern design.
• Design to be able to be used on black or white background as I want to put it on clothing

```html
<!DOCTYPE html>
<html lang="en">
<head>
<meta charset="utf-8">
<title>KVM Contracting Services – Business Card</title>
<link rel="stylesheet" href="https://fonts.googleapis.com/css2?family=Montserrat:wght@500;700&family=Asap+Condensed:wght@600&display=swap">
<style>
  :root {
    --red: #ec1f27;
    --yellow: #fbee3e;
    --black: #000000;
    --white: #ffffff;
    --backdrop: #e6e6e6;
  }
  * { margin: 0; padding: 0; box-sizing: border-box; }
  html, body {
    width: 1200px;
    height: 900px;
    overflow: hidden;
    background: var(--backdrop);
  }
  .card {
    position: absolute;
    left: 75px;
    top: 150px;
    width: 1050px;
    height: 600px;
    background: var(--black);
    overflow: hidden;
  }
  .band {
    position: absolute;
    left: 0;
    width: 100%;
    display: flex;
  }
  .band--top { top: 0; height: 43px; }
  .band--bottom { bottom: 0; height: 36px; }
  .band__yellow { background: var(--yellow); }
  .band__red { background: var(--red); }
  .band--top .band__yellow { width: 341px; }
  .band--top .band__red { flex: 1; }
  .band--bottom .band__red { width: 721px; }
  .band--bottom .band__yellow { flex: 1; }

  .rule {
    position: absolute;
    top: 320px;
    height: 2px;
    background: var(--white);
  }
  .rule--left { left: 0; width: 62px; }
  .rule--right { left: 357px; right: 0; }

  .company-name {
    position: absolute;
    left: 62px;
    top: 321px;
    width: 295px;
    transform: translateY(-50%);
    text-align: center;
    font-family: "Montserrat", sans-serif;
    font-weight: 700;
    font-size: 64px;
    line-height: 1;
    letter-spacing: 2px;
    color: var(--white);
  }

  .holder {
    position: absolute;
    left: 531px;
    top: 272px;
    font-family: "Montserrat", sans-serif;
    font-size: 34px;
    line-height: 1;
    text-transform: uppercase;
    white-space: nowrap;
  }
  .holder__first { color: var(--red); font-weight: 700; }
  .holder__last { color: var(--yellow); font-weight: 500; }

  .details {
    position: absolute;
    left: 531px;
    top: 348px;
    list-style: none;
    font-family: "Asap Condensed", sans-serif;
    font-weight: 600;
    font-size: 27px;
    line-height: 32.5px;
    white-space: nowrap;
  }
  .details__phone, .details__service { color: var(--yellow); }
  .details__speciality { color: var(--red); }
</style>
</head>
<body>
  <div class="card">
    <div class="band band--top"><span class="band__yellow"></span><span class="band__red"></span></div>

    <div class="rule rule--left"></div>
    <div class="company-name">KVM</div>
    <div class="rule rule--right"></div>

    <p class="holder"><span class="holder__first">Marcus</span> <span class="holder__last">Dellwood</span></p>
    <ul class="details">
      <li class="details__phone">0419274530</li>
      <li class="details__service">Maintenance services</li>
      <li class="details__speciality">Optic fibre and data installation</li>
    </ul>

    <div class="band band--bottom"><span class="band__red"></span><span class="band__yellow"></span></div>
  </div>
</body>
</html>
```